IT Network Consultancy - Brochure

m2 relays is a IT network consultancy based in London. We're looking for a smart, modern and professional brochure in A4 format. Our website is here: www.m2relays.co.uk. We likely will require the brochure in two formats:

PDF / Scroll Down (The most common distribution of the brochure will be PDF, which will scroll down page after page):

Page 1 - Front page
Page 2 - Portrait / scroll down
Page 3 - Portrait / scroll down
Page 4 - Portrait / scroll down
Page 5 - Portrait / scroll down
Page 6 - Back page

Side by Side / Professionally Printed:

Page 1 - Front page
Page 2/3 - Side by side
Page 4/5 - Side by side
Page 6 - Back page
Updates

Please note - I made a number of changes to the design brief after initially submitting it.

I have also increased the first prize budget from £150 to £200 (US $327)

Images may be used - no pictures of people though or anything too bright...

Reason: We're extending the deadline as we haven't received as many designs as we'd liked (one so far!)

Following a question from another designer:

We're a technology consultancy, not a technology company.  We don't need any futuristic graphics, just something that looks clean and professional.  Almost along the lines of financial services but not to traditional.

Target Market(s)

Large enterprise / global companies / corporates

Industry/Entity Type

Distribution

Requirements
Must have
• Incorporate our logo - which is attached to the project. They are in AI format (can be opened in Inkscape).

Initially the brochure is to be used specifically for our company profile / fact sheet (see attached PPT for text).

We would like to have a template we can also use for future documents.

Fonts should be simple.
Nice to have
• The project does not have to conform to the colour of our website but this should give you inspiration of the style we like.

A way to incorporate the design into MS PowerPoint, i.e. a template for corporate presentations.
Should not have
• Bright colours.

```html
<!DOCTYPE html>
<html lang="en">
<head>
<meta charset="utf-8">
<title>M2 Relays – Company Profile Brochure</title>
<link rel="stylesheet" href="https://fonts.googleapis.com/css2?family=Crimson+Text:ital,wght@0,400;0,600;0,700&display=swap">
<style>
  :root {
    --canvas: #ffffff;
    --paper: #ffffff;
    --ink: #1d1f22;
    --ink-soft: #3a3d42;
    --muted: #8c949c;
    --rule: #9aa1a8;
    --brand: #8d949b;
    --tab-1: #1f2731;
    --tab-2: #414c59;
    --tab-3: #626e7b;
    --tab-4: #8b95a0;
    --tab-5: #b7bec6;
    --tab-6: #d8dde2;
    --shadow: rgba(0,0,0,0.18);
  }
  * { box-sizing: border-box; margin: 0; padding: 0; }
  html, body {
    width: 1200px; height: 900px; overflow: hidden;
    background: var(--canvas);
    font-family: "Crimson Text", Georgia, serif;
    color: var(--ink);
  }
  .spread {
    position: relative; width: 1200px; height: 900px;
  }
  .page {
    position: absolute; top: 50px;
    width: 556px; height: 786px;
    background: var(--paper);
    border: 1px solid #2a2a2a;
    box-shadow: 2px 3px 10px var(--shadow);
  }
  .page--profile { left: 36px; }
  .page--services { left: 608px; }

  /* brand name */
  .brand {
    position: absolute;
    display: flex; align-items: center; gap: 10px;
    color: var(--brand);
    font-weight: 600;
    letter-spacing: 0.06em;
    text-transform: uppercase;
  }
  .brand__mark { width: 16px; height: 16px; background: var(--brand); }
  .page--profile .brand { left: 44px; top: 110px; font-size: 26px; }
  .page--services .brand { left: 44px; top: 48px; font-size: 26px; }

  /* service tabs */
  .tabs { position: absolute; left: 0; top: 0; list-style: none; }
  .tab {
    position: absolute;
    width: 206px; height: 34px;
    padding: 4px 0 0 10px;
    font-size: 16px;
    border-radius: 0 16px 6px 0;
    color: #fff;
  }
  .tab:nth-child(1) { left: 196px; top: 30px; background: var(--tab-1); }
  .tab:nth-child(2) { left: 216px; top: 60px; background: var(--tab-2); }
  .tab:nth-child(3) { left: 238px; top: 90px; background: var(--tab-3); }
  .tab:nth-child(4) { left: 260px; top: 120px; background: var(--tab-4); }
  .tab:nth-child(5) { left: 282px; top: 150px; background: var(--tab-5); color: var(--ink); }
  .tab:nth-child(6) { left: 304px; top: 180px; background: var(--tab-6); color: var(--ink); }

  .profile { position: absolute; left: 44px; right: 40px; top: 258px; }
  .profile h2 { font-size: 19px; font-weight: 700; margin-bottom: 6px; }
  .profile p { font-size: 17px; line-height: 1.35; color: var(--ink-soft); }
  .profile__rule {
    position: absolute; left: 44px; right: 40px; top: 398px;
    border-top: 1px solid var(--rule);
  }

  .col { position: absolute; font-size: 11.5px; line-height: 1.45; color: var(--ink-soft); }
  .col h3 { font-size: 17px; font-weight: 700; color: var(--ink); margin-bottom: 3px; }
  .col p { margin-bottom: 4px; }
  .col--values { left: 44px; top: 432px; width: 210px; }
  .col--history { left: 290px; top: 420px; width: 232px; }
  .mission { margin-top: 34px; }

  .ticks { list-style: none; }
  .ticks li { position: relative; padding-left: 12px; margin-bottom: 6px; }
  .ticks li::before {
    content: "✓"; position: absolute; left: 0; top: 0;
    color: var(--muted); font-size: 10px;
  }

  /* services page */
  .header-rule {
    position: absolute; left: 40px; right: 40px; top: 122px;
    border-top: 1px solid var(--rule);
  }
  .page-tab {
    position: absolute; left: -1px; top: 280px;
    width: 30px; height: 62px;
    background: var(--tab-5);
    border-radius: 0 31px 31px 0;
    color: #fff; font-size: 18px;
    display: flex; align-items: center; justify-content: center;
    padding-right: 6px;
  }
  .services-title {
    position: absolute; left: 44px; top: 134px; width: 230px;
    font-size: 22px; font-weight: 700; line-height: 1.05; color: var(--ink);
  }
  .svc { position: absolute; font-size: 11.5px; line-height: 1.4; color: var(--ink-soft); }
  .svc--left { left: 44px; top: 188px; width: 234px; }
  .svc--right { left: 300px; top: 134px; width: 220px; }
  .svc__group {
    position: relative; padding-left: 11px;
    color: var(--muted); font-weight: 600; font-size: 11.5px; margin: 6px 0 8px;
  }
  .svc__group::before { content: "✓"; position: absolute; left: 0; font-size: 10px; }
  .svc__list { list-style: none; padding-left: 34px; }
  .svc__item { position: relative; margin-bottom: 8px; }
  .svc__item::before {
    content: ""; position: absolute; left: -12px; top: 6px;
    width: 5px; height: 5px; border-radius: 50%; background: var(--muted);
  }
  .svc__name { color: var(--muted); font-weight: 600; }
  .svc--right .svc__list { padding-left: 14px; }
</style>
</head>
<body>
<main class="spread">

  <section class="page page--profile">
    <div class="brand"><span class="brand__mark"></span>m2 relays</div>
    <ul class="tabs">
      <li class="tab">architecture</li>
      <li class="tab">design</li>
      <li class="tab">implementation</li>
      <li class="tab">network</li>
      <li class="tab">audit</li>
      <li class="tab">team support</li>
    </ul>

    <div class="profile">
      <h2>Company Profile</h2>
      <p>M2 Relays is a London based consultancy specialising in IT networking and network security solutions. Our commitment is to build strong and lasting relationships with our customers. We aim to understand our customers’ business goals, business principles and strategic drivers to ensure that our delivery is aligned and relevant.</p>
    </div>
    <div class="profile__rule"></div>

    <div class="col col--values">
      <h3>Values</h3>
      <p>M2 is founded on the following core values:</p>
      <ul class="ticks">
        <li>Integrity first</li>
        <li>Dedication to our customer’s success</li>
        <li>Driven by technical leadership</li>
      </ul>
      <div class="mission">
        <h3>Mission Statement</h3>
        <p>M2’s mission is to by exceeding all expectations in technical knowledge, professional standards and delivery.</p>
      </div>
    </div>

    <div class="col col--history">
      <h3>History</h3>
      <p>While M2 is a young organisation, our founders have extensive experience. From consultancy services and project delivery, to strategy and architectural guidance, we have:</p>
      <ul class="ticks">
        <li>Delivered large and complex projects on time, on budget and to specification</li>
        <li>Developed scalable, reliable and integrated network architectures</li>
        <li>Produced technology roadmaps, defined strategic frameworks, and managed technology integration</li>
        <li>Optimised infrastructure and delivered operational efficiency improvements</li>
        <li>Created innovative, simple and elegant solutions</li>
      </ul>
    </div>
  </section>

  <section class="page page--services">
    <div class="brand"><span class="brand__mark"></span>m2 relays</div>
    <div class="header-rule"></div>
    <div class="page-tab">2</div>

    <h2 class="services-title">Network Consultancy services</h2>

    <div class="svc svc--left">
      <div class="svc__group">Architecture</div>
      <ul class="svc__list">
        <li class="svc__item"><span class="svc__name">Network Architecture</span> – Strategic principles and business objectives are translated into architecture, deployment guides and templates with the aim of achieving predictable and repeatable management, operational and deployment processes.</li>
        <li class="svc__item"><span class="svc__name">Technology Strategy Development</span> – M2 will use its understanding of the customer’s and its competitor’s environment, vendor technology roadmaps and information technology strategy in general to compile coherent, consistent and integrated technology strategies.</li>
        <li class="svc__item"><span class="svc__name">Business Requirements Development</span> – Recognising that high-level business requirements drive technical engineering tasks, M2 will engage with stakeholders and develop a comprehensive view of the requirements and translate these into design criteria.</li>
      </ul>
      <div class="svc__group">Network Design</div>
      <ul class="svc__list">
        <li class="svc__item">Using best practices and comprehensive real-world experience, M2 network designs are delivered to specification. Total cost of ownership and risk are reduced while agility and scalability are increased.</li>
      </ul>
    </div>

    <div class="svc svc--right">
      <ul class="svc__list">
        <li class="svc__item"><span class="svc__name">Design Reviews</span> – Through a combination of experience and industry best-practices, M2 will review the customer’s designs with a critical, knowledgeable and objective point of view and make the relevant recommendations.</li>
        <li class="svc__item"><span class="svc__name">Proof of Concept and Testing</span> – M2 will engage with IT departments, business units, clients and vendors to complete thorough technology proof of concepts, vendor bake-offs, produce test plans and manage regression testing.</li>
      </ul>
    </div>
  </section>

</main>
</body>
</html>
```